Cloud Hosting Provider Web Site

We need to create the design for Nimbo-Pails.net a new Cloud Hosting Provider Website.

We already have a logo and a draft website with preliminary content showing the desired structure for the final web site.

I need a design for the Home Page and all 10 Internal web pages currently linked from the draft home page.

The documentation site (/docs) Customer Portal (/portal) and Support site (/support) are not part of this design project.

We need images to illustrate all pages which of course need to be consistent with the content. Please read carefully the text of each page in the draft web site to understand the purpose of each page and illustrate it accordingly.

All pages must be illustrated with images, I do not want any single page with just text.

I want to maintain the slides idea of the draft website home page.

The web site must look professional, we are competitors of huge companies like tallow grid systems (tgs.tallowgrid.com), Velquist Oriel (oriel.velquist.com) and DuneLoft (www.duneloft.com) so we need to look as serious as them.

You may download the draft web site pages to style them, I need fully finalized HTML / CSS and image files.

A top link bar and link footer must be included in every page.

Also the web site will have the possibility to start a chat conversation with a sales agent, so a graphical link to do so must be included in the design, together with a chat window design (including HTML/CSS)

Information for accessing the draft web site follows:

URL: www.nimbo-pails.net
username: design
password: QOPqop987654

If you need any additional information please let me know.

```html
<!DOCTYPE html>
<html lang="en">
<head>
<meta charset="utf-8">
<title>Nimbo-Pails.net – Private Cloud Hosting</title>
<link href="https://fonts.googleapis.com/css2?family=Roboto:wght@300;400;500;700&family=Oswald:wght@300&display=swap" rel="stylesheet">
<style>
:root{
  --sky:#1ba3dc;
  --navy:#123a5c;
  --ink:#333;
  --muted:#8a8a8a;
  --foot:#231f20;
  --foot-line:#4a4647;
  --foot-text:#d0d0d0;
  --c-orange:#f47a1f;
  --c-yellow:#e2bf00;
  --c-pink:#d72f5f;
  --c-green:#38b26f;
  --c-purple:#9a3399;
  --c-olive:#c59b00;
  --c-slate:#4b4845;
  --c-blue:#0c5a94;
  --c-maroon:#781f3c;
}
*{box-sizing:border-box;margin:0;padding:0}
html,body{width:1200px;height:2308px;overflow:hidden}
body{font-family:'Roboto',sans-serif;color:var(--ink);background:#fff;position:relative}
a{color:inherit;text-decoration:none}

/* header */
.site-header{height:111px;position:relative}
.brand{position:absolute;left:98px;top:40px;display:flex;align-items:center;gap:10px;font-size:22px;font-weight:700;color:#0d3f6e}
.brand-dot{width:26px;height:26px;border-radius:50%;background:var(--sky)}
.live-help{position:absolute;left:815px;top:34px;display:flex;align-items:center;gap:10px}
.live-help svg{width:30px;height:36px}
.live-help .label{font-size:12px;font-weight:500;color:var(--sky);letter-spacing:.2px}
.live-help .phone{font-size:18px;color:#222;margin-top:2px}
.chat-btn{position:absolute;left:985px;top:39px;width:115px;height:29px;background:var(--sky);color:#fff;border-radius:3px;font-size:12px;display:flex;align-items:center;justify-content:center;gap:6px}
.chat-btn svg{width:16px;height:14px}

/* nav */
.main-nav{height:60px;background:var(--sky);position:relative}
.main-nav a{position:absolute;top:0;height:60px;display:flex;align-items:center;font-size:12.5px;font-weight:500;color:#fff;text-transform:uppercase}
.main-nav .active{left:98px;width:74px;justify-content:center;background:var(--navy);border-bottom:3px solid #fff}
.main-nav .login{left:958px;top:11px;height:38px;width:142px;justify-content:center;background:var(--navy);border-radius:2px}

/* hero */
.hero{height:589px;position:relative;overflow:hidden}
.hero-art{position:absolute;inset:0;background:radial-gradient(circle at 36% 40%,#1f8ed0 0%,#0f3f74 22%,#0a1f3c 50%,#050b17 100%)}
.hero-arrow{position:absolute;top:273px;width:44px;height:44px;border:2px solid rgba(255,255,255,.35);border-radius:50%}
.hero-arrow svg{width:100%;height:100%}
.hero-arrow.prev{left:44px}.hero-arrow.next{left:1109px}
.hero-copy{position:absolute;left:380px;top:428px;width:702px;text-align:center;color:#fff}
.hero-copy h1{font-family:'Oswald',sans-serif;font-weight:300;font-size:38px;letter-spacing:-.3px;line-height:1}
.hero-copy p{margin-top:18px;font-size:13px;line-height:21px;font-weight:300}

/* welcome */
.welcome{text-align:center;padding-top:44px}
.welcome h2{font-size:26px;font-weight:500;color:#3a3a3a}
.welcome p{width:930px;margin:18px auto 0;font-size:11.5px;line-height:20px;color:var(--muted);font-weight:300}
.btn{display:inline-flex;align-items:center;justify-content:center;background:var(--sky);color:#fff;font-size:12px;font-weight:500;border-radius:3px;text-transform:uppercase}
.welcome .btn{width:96px;height:34px;margin-top:24px}

/* service cards */
.service-grid{position:absolute;left:100px;top:1072px;width:997px;display:grid;grid-template-columns:repeat(3,317px);column-gap:23px;row-gap:106px}
.card{height:216px;position:relative;border:3px solid #fff;box-shadow:0 0 0 1px #ddd;text-align:center;color:#fff}
.card .badge{position:absolute;left:50%;top:-66px;width:132px;height:132px;margin-left:-66px;border-radius:50%;border:4px solid #fff;display:flex;align-items:center;justify-content:center}
.card .badge span{width:64px;height:64px;border-radius:50%;background:rgba(255,255,255,.22)}
.card h3{position:absolute;left:20px;right:20px;bottom:82px;font-size:14.5px;font-weight:500;line-height:20px;text-transform:uppercase}
.card .btn{position:absolute;left:50%;top:149px;margin-left:-57px;width:114px;height:33px;gap:5px;font-size:12px}
.card .btn svg{width:13px;height:15px}
.orange{background:var(--c-orange)}.yellow{background:var(--c-yellow)}.pink{background:var(--c-pink)}
.green{background:var(--c-green)}.purple{background:var(--c-purple)}.olive{background:var(--c-olive)}
.slate{background:var(--c-slate)}.blue{background:var(--c-blue)}.maroon{background:var(--c-maroon)}

/* footer */
.site-footer{position:absolute;left:0;top:1984px;width:1200px;height:324px;background:var(--foot);color:var(--foot-text)}
.foot-col{position:absolute;top:60px}
.foot-col h4{font-size:14.5px;font-weight:500;color:#fff;text-transform:uppercase}
.foot-col h4.plain{text-transform:none}
.foot-col ul{list-style:none;margin-top:33px}
.foot-col li{font-size:11.5px;line-height:22px}
.foot-services li::before{content:"";display:inline-block;border-left:5px solid var(--sky);border-top:4px solid transparent;border-bottom:4px solid transparent;margin-right:6px}
.divider{position:absolute;top:52px;width:1px;height:170px;background:var(--foot-line)}
.newsletter .sub{font-size:11px;margin-top:6px;color:#aaa}
.newsletter input,.newsletter textarea{display:block;width:239px;border:0;background:#e8e8e8;font-family:inherit;font-size:11.5px;font-style:italic;padding:0 12px;color:#999}
.newsletter input{height:34px;margin-top:9px}
.newsletter input:first-of-type{margin-top:17px}
.newsletter textarea{height:47px;margin-top:8px;padding-top:12px;resize:none}
.newsletter .btn{position:absolute;left:140px;top:189px;width:99px;height:34px;border:0;border-radius:0;font-family:inherit;font-size:12.5px}
.contact li{line-height:21px}
.copyright{position:absolute;left:100px;top:276px;font-size:10.5px;color:#aaa}
</style>
</head>
<body>

<header class="site-header">
  <a class="brand" href="#"><span class="brand-dot"></span>Nimbo-Pails.net</a>
  <div class="live-help">
    <svg viewBox="0 0 30 36" aria-hidden="true"><circle cx="15" cy="11" r="8" fill="#1c2b3a"/><path d="M3 36c0-9 5-14 12-14s12 5 12 14z" fill="#1c2b3a"/><path d="M5 12a10 10 0 0 1 20 0" stroke="#1c2b3a" stroke-width="2.5" fill="none"/><rect x="3" y="11" width="4" height="7" rx="1.5" fill="#1c2b3a"/></svg>
    <div><div class="label">LIVE HELP ONLINE</div><div class="phone">19_400_62000</div></div>
  </div>
  <a class="chat-btn" href="#">Chat with us!
    <svg viewBox="0 0 16 14" aria-hidden="true"><ellipse cx="6.5" cy="5.5" rx="6" ry="4.5" fill="#fff"/><ellipse cx="10.5" cy="9" rx="5" ry="4" fill="#fff" stroke="#1ba3dc"/></svg>
  </a>
</header>

<nav class="main-nav">
  <a class="active" href="#">Home</a>
  <a href="#" style="left:254px">Use cases</a>
  <a href="#" style="left:398px">Cloud services</a>
  <a href="#" style="left:578px">Pail's infrastructure</a>
  <a href="#" style="left:816px">Our company</a>
  <a class="login" href="#">Customer login</a>
</nav>

<section class="hero">
  <div class="hero-art" role="img" aria-label="Hand drawing a glowing cloud network linking screens and devices on a dark blue background"></div>
  <a class="hero-arrow prev" href="#" aria-label="Previous slide"><svg viewBox="0 0 44 44"><path d="M25 13l-9 9 9 9" stroke="rgba(255,255,255,.4)" stroke-width="2.5" fill="none"/></svg></a>
  <a class="hero-arrow next" href="#" aria-label="Next slide"><svg viewBox="0 0 44 44"><path d="M19 13l9 9-9 9" stroke="rgba(255,255,255,.4)" stroke-width="2.5" fill="none"/></svg></a>
  <div class="hero-copy">
    <h1>CREATE YOUR OWN PRIVATE CLOUD, BRICK BY BRICK</h1>
    <p>Already spending more than US$ 1.000 per month in the public cloud? - Start saving money by creating your<br>own private cloud. - Easy to use web based management software</p>
  </div>
</section>

<section class="welcome">
  <h2>WELCOME TO NIMBO-PAILS</h2>
  <p>There are many variations of passages of Lorem Ipsum available, but the majority have suffered alteration in some form, by injected humour, or randomised words which don't look even slightly believable. If you are going to use a passage of Lorem Ipsum, you need to be sure there isn't anything embarrassing hidden in the middle of text. All the Lorem Ipsum generators on the Internet tend to repeat predefined chunks as necessary, making this the first true generator on the Internet.</p>
  <a class="btn" href="#">Read more</a>
</section>

<section class="service-grid">
  <article class="card orange"><div class="badge orange" role="img" aria-label="Gear icon"><span></span></div><h3>Start your own<br>hosting business</h3><a class="btn" href="#"><svg viewBox="0 0 13 15"><path d="M4 1.5v8l-2-1.5-1 1 3.5 5h6l1-5-4-1V1.5z" fill="none" stroke="#fff" stroke-width="1.2"/></svg>Click here</a></article>
  <article class="card yellow"><div class="badge yellow" role="img" aria-label="Virtualization icon"><span></span></div><h3>Virtualize your current<br>physical infraestructure</h3><a class="btn" href="#"><svg viewBox="0 0 13 15"><path d="M4 1.5v8l-2-1.5-1 1 3.5 5h6l1-5-4-1V1.5z" fill="none" stroke="#fff" stroke-width="1.2"/></svg>Click here</a></article>
  <article class="card pink"><div class="badge pink" role="img" aria-label="Moving truck icon"><span></span></div><h3>Moving from the public<br>to the private cloud</h3><a class="btn" href="#"><svg viewBox="0 0 13 15"><path d="M4 1.5v8l-2-1.5-1 1 3.5 5h6l1-5-4-1V1.5z" fill="none" stroke="#fff" stroke-width="1.2"/></svg>Click here</a></article>
  <article class="card green"><div class="badge green" role="img" aria-label="Piggy bank icon"><span></span></div><h3>Saving money with the<br>private cloud</h3><a class="btn" href="#"><svg viewBox="0 0 13 15"><path d="M4 1.5v8l-2-1.5-1 1 3.5 5h6l1-5-4-1V1.5z" fill="none" stroke="#fff" stroke-width="1.2"/></svg>Click here</a></article>
  <article class="card purple"><div class="badge purple" role="img" aria-label="Cloud icon"><span></span></div><h3>Nimbo-Pails technical<br>features</h3><a class="btn" href="#"><svg viewBox="0 0 13 15"><path d="M4 1.5v8l-2-1.5-1 1 3.5 5h6l1-5-4-1V1.5z" fill="none" stroke="#fff" stroke-width="1.2"/></svg>Click here</a></article>
  <article class="card olive"><div class="badge olive" role="img" aria-label="Document icon"><span></span></div><h3>Documentation: introducing<br>Nimbo-Pails virtual datacenter<br>management platform</h3><a class="btn" href="#"><svg viewBox="0 0 13 15"><path d="M4 1.5v8l-2-1.5-1 1 3.5 5h6l1-5-4-1V1.5z" fill="none" stroke="#fff" stroke-width="1.2"/></svg>Click here</a></article>
  <article class="card slate"><div class="badge slate" role="img" aria-label="Cloud icon"><span></span></div><h3>Cloud services</h3><a class="btn" href="#"><svg viewBox="0 0 13 15"><path d="M4 1.5v8l-2-1.5-1 1 3.5 5h6l1-5-4-1V1.5z" fill="none" stroke="#fff" stroke-width="1.2"/></svg>Click here</a></article>
  <article class="card blue"><div class="badge blue" role="img" aria-label="Round-the-clock support clock icon"><span></span></div><h3>7x24x365 support</h3><a class="btn" href="#"><svg viewBox="0 0 13 15"><path d="M4 1.5v8l-2-1.5-1 1 3.5 5h6l1-5-4-1V1.5z" fill="none" stroke="#fff" stroke-width="1.2"/></svg>Click here</a></article>
  <article class="card maroon"><div class="badge maroon" role="img" aria-label="Money bag icon"><span></span></div><h3>Pricing</h3><a class="btn" href="#"><svg viewBox="0 0 13 15"><path d="M4 1.5v8l-2-1.5-1 1 3.5 5h6l1-5-4-1V1.5z" fill="none" stroke="#fff" stroke-width="1.2"/></svg>Click here</a></article>
</section>

<footer class="site-footer">
  <div class="foot-col" style="left:100px">
    <h4>Company</h4>
    <ul><li>Home</li><li>Use cases</li><li>Cloud services</li><li>Pail's Infrastructure</li><li>Our company</li></ul>
  </div>
  <div class="divider" style="left:255px"></div>
  <div class="foot-col foot-services" style="left:312px">
    <h4 class="plain">Featured Services</h4>
    <ul style="margin-top:29px"><li>Residential Cleaning</li><li>Commercial Cleaning</li><li>Green Cleaning</li><li>Move-in/out Cleaning</li><li>Vacant Home Cleaning</li><li>Window Cleaning</li></ul>
  </div>
  <div class="divider" style="left:492px"></div>
  <form class="foot-col newsletter" style="left:552px">
    <h4>Sign to newsletter</h4>
    <div class="sub">Join our confidential network and be the</div>
    <input type="text" placeholder="Name">
    <input type="email" placeholder="Email">
    <textarea placeholder="message..."></textarea>
    <button class="btn" type="button">Subscribe</button>
  </form>
  <div class="divider" style="left:857px"></div>
  <div class="foot-col contact" style="left:914px">
    <h4>Contact us</h4>
    <ul><li>14 Larkspur Row, Fenwick Hollow,</li><li>Phone: 19_400_62000</li><li>Mobile: 19_400_62000</li><li>Fax: 04 5127 3308</li><li>Email: info@nimbo-pails.com.</li></ul>
  </div>
  <div class="copyright">Copyright © 2015 nimbo-pails - all rights reserved</div>
</footer>

</body>
</html>
```